Plakate für Podologie - Medizinische Fusspflege
Zielgruppe
Podologie - Medizinische Fusspflege. Zielgruppe sind Kinder bis und mit ältere Menschen.
Aufgabenstellung
Möchte ein modernes, aber auch klassisches Design, dass Professionalität & medizinische Fundiertheit ausstrahlt. Man soll sehen, dass es medizinisch ist und nicht verwechselbar mit kosmetischer Fusspflege.

```html
<!DOCTYPE html>
<html lang="de">
<head>
<meta charset="utf-8">
<title>PedaVita – Plakate Medizinische Fusspflege</title>
<link rel="stylesheet" href="https://fonts.googleapis.com/css2?family=Red+Hat+Display:wght@500;600;700;800;900&display=swap">
<style>
  :root {
    --teal: #17564f;
    --green: #5aa843;
    --green-text: #4b9c38;
    --paper: #ffffff;
    --stage: #e8eaec;
    --photo-a: #e9d3b4;
    --photo-b: #cfe2f1;
    --photo-c: #7aa9d6;
    --photo-d: #2d3a4f;
  }
  * { box-sizing: border-box; margin: 0; padding: 0; }
  html, body { width: 1200px; height: 800px; overflow: hidden; }
  body {
    background: var(--stage);
    font-family: "Red Hat Display", Arial, sans-serif;
    position: relative;
  }
  .poster {
    position: absolute;
    top: 40px;
    width: 510px;
    height: 720px;
    background: var(--paper);
    overflow: hidden;
    box-shadow: 0 6px 22px rgba(0,0,0,.14);
  }
  .poster--a { left: 65px; }
  .poster--b { left: 625px; }

  .hero-photo {
    position: absolute; left: 0; top: 0; width: 510px; height: 250px;
    background:
      radial-gradient(ellipse 140px 110px at 290px 80px, var(--photo-c) 0%, rgba(122,169,214,0) 100%),
      radial-gradient(ellipse 120px 160px at 440px 120px, var(--photo-d) 0%, rgba(45,58,79,0) 100%),
      linear-gradient(90deg, var(--photo-a) 0%, var(--photo-a) 22%, var(--photo-b) 45%, #dfe8f0 70%, #8a93a0 100%);
  }
  .hero-curve { position: absolute; left: 0; top: 150px; width: 510px; height: 110px; }

  .headline {
    position: absolute; left: 41px; top: 203px;
    display: flex; flex-direction: column; align-items: flex-start;
  }
  .headline__line {
    color: #fff; font-weight: 900; font-size: 32px; line-height: 1;
    letter-spacing: .3px; padding: 5px 10px 6px 14px;
    background: var(--teal); border-radius: 8px;
  }
  .poster--b .headline__line--accent { background: var(--green); margin-top: 6px; }
  .poster--b .headline { top: 188px; }

  .subline {
    position: absolute; left: 57px; top: 300px;
    font-size: 18.5px; font-weight: 700; line-height: 1.25;
  }
  .subline__main { color: var(--teal); display: block; }
  .subline__accent { color: var(--green-text); display: block; }

  .quality-badge {
    position: absolute; left: 47px; top: 375px; width: 140px; height: 176px;
  }
  .quality-badge svg { position: absolute; inset: 0; }
  .quality-badge__claim {
    position: absolute; left: 16px; top: 20px;
    color: #fff; font-size: 15px; font-weight: 600; line-height: 1.25;
  }
  .quality-badge__seal {
    position: absolute; left: 0; width: 140px; top: 104px; text-align: center;
    color: #fff; font-size: 13px; font-weight: 700; line-height: 1.25; letter-spacing: .3px;
  }
  .quality-badge__stars { display: block; font-size: 9px; letter-spacing: 2px; margin-top: 6px; }

  .service-list {
    position: absolute; left: 236px; top: 384px; list-style: none;
  }
  .service-list li {
    display: flex; align-items: flex-start; gap: 10px;
    color: var(--teal); font-size: 14.5px; font-weight: 700; line-height: 1.2;
    margin-bottom: 13px;
  }
  .service-list svg { flex: 0 0 21px; width: 21px; height: 21px; margin-top: -2px; }

  .footer-info {
    position: absolute; left: 41px; top: 604px; right: 20px; display: flex; align-items: flex-start;
  }
  .brand { display: flex; align-items: center; gap: 8px; width: 182px; }
  .brand__dot { width: 26px; height: 26px; border-radius: 50%; background: var(--green); flex: 0 0 26px; }
  .brand__text { display: flex; flex-direction: column; }
  .brand__name { color: var(--teal); font-size: 24px; font-weight: 800; line-height: 1; }
  .brand__tag { color: var(--teal); font-size: 7.5px; font-weight: 600; letter-spacing: .8px; margin-top: 4px; }
  .contact-block { color: var(--teal); font-size: 10px; font-weight: 600; line-height: 1.55; }
  .contact-block--address { width: 136px; }
  .contact-block__label { font-weight: 800; }
  .contact-block__row { display: flex; align-items: center; gap: 5px; }
  .contact-block__row svg { width: 10px; height: 10px; }

  .cta {
    position: absolute; bottom: 0; height: 36px;
    background: var(--teal); color: #fff;
    font-size: 14px; font-weight: 800; letter-spacing: .8px;
    display: flex; align-items: center; justify-content: center;
  }
  .poster--a .cta { left: 0; right: 0; border-radius: 8px 8px 0 0; }
  .poster--b .cta { left: 96px; width: 316px; border-radius: 8px 8px 0 0; }
</style>
</head>
<body>

<section class="poster poster--a">
  <div class="hero-photo" role="img" aria-label="Foto: Podologin mit blauen Handschuhen behandelt einen Fuss"></div>
  <svg class="hero-curve" viewBox="0 0 510 110" preserveAspectRatio="none" aria-hidden="true">
    <path d="M0 80 C120 40 300 70 510 95 L510 110 L0 110 Z" fill="#fff"/>
  </svg>
  <h1 class="headline">
    <span class="headline__line">IHRE FÜSSE.</span>
    <span class="headline__line headline__line--accent">UNSERE KOMPETENZ.</span>
  </h1>
  <p class="subline">
    <span class="subline__main">Medizinische Fussbehandlungen für</span>
    <span class="subline__accent">Ihre Gesundheit und Lebensqualität.</span>
  </p>
  <div class="quality-badge">
    <svg viewBox="0 0 140 176" aria-hidden="true">
      <path d="M4 0 H136 Q140 0 140 4 V150 L70 176 L0 150 V4 Q0 0 4 0 Z" fill="#5aa843"/>
      <path d="M10 88 H130 V148 L70 168 L10 148 Z" fill="#17564f"/>
    </svg>
    <p class="quality-badge__claim">Fachgerecht.<br>Hygienisch.<br>Modern.</p>
    <p class="quality-badge__seal">ZERTIFIZIERTE<br>PODOLOGEN<span class="quality-badge__stars">★★★</span></p>
  </div>
  <ul class="service-list">
    <li><svg viewBox="0 0 20 20"><circle cx="10" cy="10" r="10" fill="#17564f"/><path d="M5.5 10.5 L8.7 13.5 L14.5 7" stroke="#fff" stroke-width="2.2" fill="none" stroke-linecap="round" stroke-linejoin="round"/></svg>Medizinische Fusspflege</li>
    <li><svg viewBox="0 0 20 20"><circle cx="10" cy="10" r="10" fill="#17564f"/><path d="M5.5 10.5 L8.7 13.5 L14.5 7" stroke="#fff" stroke-width="2.2" fill="none" stroke-linecap="round" stroke-linejoin="round"/></svg>Nagelkorrektur</li>
    <li><svg viewBox="0 0 20 20"><circle cx="10" cy="10" r="10" fill="#17564f"/><path d="M5.5 10.5 L8.7 13.5 L14.5 7" stroke="#fff" stroke-width="2.2" fill="none" stroke-linecap="round" stroke-linejoin="round"/></svg>Eingewachsene Nägel</li>
    <li><svg viewBox="0 0 20 20"><circle cx="10" cy="10" r="10" fill="#17564f"/><path d="M5.5 10.5 L8.7 13.5 L14.5 7" stroke="#fff" stroke-width="2.2" fill="none" stroke-linecap="round" stroke-linejoin="round"/></svg>Hornhaut &amp; Hühneraugen</li>
    <li><svg viewBox="0 0 20 20"><circle cx="10" cy="10" r="10" fill="#17564f"/><path d="M5.5 10.5 L8.7 13.5 L14.5 7" stroke="#fff" stroke-width="2.2" fill="none" stroke-linecap="round" stroke-linejoin="round"/></svg>Diabetische Fussversorgung</li>
    <li><svg viewBox="0 0 20 20"><circle cx="10" cy="10" r="10" fill="#17564f"/><path d="M5.5 10.5 L8.7 13.5 L14.5 7" stroke="#fff" stroke-width="2.2" fill="none" stroke-linecap="round" stroke-linejoin="round"/></svg><span>Auch für Risikopatienten,<br>Kinder und Sportler</span></li>
  </ul>
  <div class="footer-info">
    <div class="brand">
      <span class="brand__dot"></span>
      <span class="brand__text"><span class="brand__name">PedaVita</span><span class="brand__tag">MEDIZINISCHE PODOLOGIE</span></span>
    </div>
    <div class="contact-block contact-block--address">
      <span class="contact-block__label">Adresse:</span><br>
      Praxis Lindenweg 24<br>4410 Liestal
    </div>
    <div class="contact-block">
      <span class="contact-block__label">Kontakt:</span>
      <div class="contact-block__row"><svg viewBox="0 0 10 10"><path d="M2 1 L4 1 L4.6 3 L3.4 4 Q4.4 5.8 6 6.6 L7 5.4 L9 6 L9 8 Q5 9 1 3 Z" fill="#5aa843"/></svg>+41 61 482 37 90</div>
      <div class="contact-block__row"><svg viewBox="0 0 10 10"><circle cx="5" cy="5" r="4.2" fill="none" stroke="#5aa843" stroke-width="1"/><path d="M1 5 H9 M5 1 Q2.5 5 5 9 M5 1 Q7.5 5 5 9" stroke="#5aa843" stroke-width=".8" fill="none"/></svg>www.pedavita.ch</div>
    </div>
  </div>
  <div class="cta">JETZT TERMIN VEREINBAREN!</div>
</section>

<section class="poster poster--b">
  <div class="hero-photo" role="img" aria-label="Foto: Podologin mit blauen Handschuhen behandelt einen Fuss"></div>
  <svg class="hero-curve" viewBox="0 0 510 110" preserveAspectRatio="none" aria-hidden="true">
    <path d="M0 80 C120 40 300 70 510 95 L510 110 L0 110 Z" fill="#fff"/>
  </svg>
  <h1 class="headline">
    <span class="headline__line">IHRE FÜSSE.</span>
    <span class="headline__line headline__line--accent">UNSERE KOMPETENZ.</span>
  </h1>
  <p class="subline">
    <span class="subline__main">Medizinische Fussbehandlungen für</span>
    <span class="subline__accent">Ihre Gesundheit und Lebensqualität.</span>
  </p>
  <div class="quality-badge">
    <svg viewBox="0 0 140 176" aria-hidden="true">
      <path d="M4 0 H136 Q140 0 140 4 V150 L70 176 L0 150 V4 Q0 0 4 0 Z" fill="#5aa843"/>
      <path d="M10 88 H130 V148 L70 168 L10 148 Z" fill="#17564f"/>
    </svg>
    <p class="quality-badge__claim">Fachgerecht.<br>Hygienisch.<br>Modern.</p>
    <p class="quality-badge__seal">ZERTIFIZIERTE<br>PODOLOGEN<span class="quality-badge__stars">★★★</span></p>
  </div>
  <ul class="service-list">
    <li><svg viewBox="0 0 20 20"><circle cx="10" cy="10" r="10" fill="#17564f"/><path d="M5.5 10.5 L8.7 13.5 L14.5 7" stroke="#fff" stroke-width="2.2" fill="none" stroke-linecap="round" stroke-linejoin="round"/></svg>Medizinische Fusspflege</li>
    <li><svg viewBox="0 0 20 20"><circle cx="10" cy="10" r="10" fill="#17564f"/><path d="M5.5 10.5 L8.7 13.5 L14.5 7" stroke="#fff" stroke-width="2.2" fill="none" stroke-linecap="round" stroke-linejoin="round"/></svg>Nagelkorrektur</li>
    <li><svg viewBox="0 0 20 20"><circle cx="10" cy="10" r="10" fill="#17564f"/><path d="M5.5 10.5 L8.7 13.5 L14.5 7" stroke="#fff" stroke-width="2.2" fill="none" stroke-linecap="round" stroke-linejoin="round"/></svg>Eingewachsene Nägel</li>
    <li><svg viewBox="0 0 20 20"><circle cx="10" cy="10" r="10" fill="#17564f"/><path d="M5.5 10.5 L8.7 13.5 L14.5 7" stroke="#fff" stroke-width="2.2" fill="none" stroke-linecap="round" stroke-linejoin="round"/></svg>Hornhaut &amp; Hühneraugen</li>
    <li><svg viewBox="0 0 20 20"><circle cx="10" cy="10" r="10" fill="#17564f"/><path d="M5.5 10.5 L8.7 13.5 L14.5 7" stroke="#fff" stroke-width="2.2" fill="none" stroke-linecap="round" stroke-linejoin="round"/></svg>Diabetische Fussversorgung</li>
    <li><svg viewBox="0 0 20 20"><circle cx="10" cy="10" r="10" fill="#17564f"/><path d="M5.5 10.5 L8.7 13.5 L14.5 7" stroke="#fff" stroke-width="2.2" fill="none" stroke-linecap="round" stroke-linejoin="round"/></svg><span>Auch für Risikopatienten,<br>Kinder und Sportler</span></li>
  </ul>
  <div class="footer-info">
    <div class="brand">
      <span class="brand__dot"></span>
      <span class="brand__text"><span class="brand__name">PedaVita</span><span class="brand__tag">MEDIZINISCHE PODOLOGIE</span></span>
    </div>
    <div class="contact-block contact-block--address">
      <span class="contact-block__label">Adresse:</span><br>
      Praxis Lindenweg 24<br>4410 Liestal
    </div>
    <div class="contact-block">
      <span class="contact-block__label">Kontakt:</span>
      <div class="contact-block__row"><svg viewBox="0 0 10 10"><path d="M2 1 L4 1 L4.6 3 L3.4 4 Q4.4 5.8 6 6.6 L7 5.4 L9 6 L9 8 Q5 9 1 3 Z" fill="#5aa843"/></svg>+41 61 482 37 90</div>
      <div class="contact-block__row"><svg viewBox="0 0 10 10"><circle cx="5" cy="5" r="4.2" fill="none" stroke="#5aa843" stroke-width="1"/><path d="M1 5 H9 M5 1 Q2.5 5 5 9 M5 1 Q7.5 5 5 9" stroke="#5aa843" stroke-width=".8" fill="none"/></svg>www.pedavita.ch</div>
    </div>
  </div>
  <div class="cta">JETZT TERMIN VEREINBAREN!</div>
</section>

</body>
</html>
```